Business card design needed

I am a free lance management consultant looking to have some professionally designed business cards created.
If possible if i could have some bullet points or something with a list of my services that would be great.
Services are:
- Strategic Planning
- Process Improvement
- Change Management
- IT Solutions & Implementation
- IT Consulting
- Web Solutions
Target Market(s)
Business Owners and Operators
Industry/Entity Type
Business
Contact Information for Business Card
Peter Whitlock
PW Consulting
0438 516 274
PETER@PETERWHITLOCK.EXAMPLE
www.peterwhitlock.example
Logo Text
PW Consulting
Logo styles of interest
Pictorial/Combination Logo
Wordmark Logo
Lettermark Logo
Look and feel
Each slider illustrates characteristics of the customer's brand and the style your logo design should communicate.

```html
<!DOCTYPE html>
<html lang="en">
<head>
<meta charset="utf-8">
<title>Peter Whitlock – Business Card</title>
<link href="https://fonts.googleapis.com/css2?family=Montserrat:wght@600&family=Questrial&display=swap" rel="stylesheet">
<style>
  :root {
    --card-bg: #2d3439;
    --accent-orange: #f0662a;
    --accent-green: #72b843;
    --service-green: #8cc63f;
    --text-light: #f2f4f5;
    --tab-text: #2d3439;
  }
  * { margin: 0; padding: 0; box-sizing: border-box; }
  html, body {
    width: 1200px;
    height: 694px;
    overflow: hidden;
    background: var(--card-bg);
  }
  .card {
    position: relative;
    width: 1200px;
    height: 694px;
    background: var(--card-bg);
    font-family: "Questrial", sans-serif;
    color: var(--text-light);
  }
  .name-badge {
    position: absolute;
    left: 97px;
    top: 120px;
    height: 59px;
    padding: 0 20px;
    display: flex;
    align-items: center;
    background: var(--accent-orange);
    border-radius: 9px;
    font-family: "Montserrat", sans-serif;
    font-weight: 600;
    font-size: 37px;
    letter-spacing: 0.5px;
    color: #ffffff;
    text-transform: uppercase;
  }
  .contact {
    position: absolute;
    left: 106px;
    top: 212px;
    display: grid;
    grid-template-columns: auto auto;
    row-gap: 16px;
    font-size: 31px;
    line-height: 1.3;
  }
  .contact .sep { padding: 0 12px; }
  .contact .website { grid-column: 2; }
  .services-tab {
    position: absolute;
    left: 75px;
    top: 407px;
    width: 40px;
    height: 203px;
    background: var(--accent-green);
    display: flex;
    align-items: center;
    justify-content: center;
  }
  .services-tab span {
    transform: rotate(-90deg);
    white-space: nowrap;
    font-size: 28px;
    letter-spacing: 1px;
    color: var(--tab-text);
  }
  .services {
    position: absolute;
    top: 436px;
    list-style: none;
    font-size: 34px;
    line-height: 50px;
    color: var(--service-green);
  }
  .services li::before { content: "-"; padding-right: 16px; }
  .services.col-left { left: 138px; }
  .services.col-right { left: 586px; }
</style>
</head>
<body>
  <div class="card">
    <div class="name-badge">Peter Whitlock</div>

    <div class="contact">
      <div class="contact-line">PW Consulting<span class="sep">|</span>0438 516 274<span class="sep">|</span></div>
      <div class="email">peter@peterwhitlock.example</div>
      <div class="website">www.peterwhitlock.example</div>
    </div>

    <div class="services-tab"><span>SERVICES</span></div>

    <ul class="services col-left">
      <li>Strategic Planning</li>
      <li>Process Improvement</li>
      <li>Change Management</li>
    </ul>
    <ul class="services col-right">
      <li>IT Solutions &amp; Implementation</li>
      <li>IT Consulting</li>
      <li>Web Solutions</li>
    </ul>
  </div>
</body>
</html>
```